House Church design model for faith-based organization

A design is needed for a house church model (Christian, faith-based). I’m looking for a graphic to convey four house church hallmarks showing the balance of member engagement. The four-part model includes - God’s Presence, Community, Discipleship, Outreach. The model should consist of the text for the four parts and the words - House Church

Perhaps a circular/modular design with House Church in the center. Using equally-sized interlocking slices or winged parts (graphically speaking, but not angelic wings) may help convey a balanced approach. It isn’t a process and should not appear in progressive steps, but the order (as listed) is used when explaining the concept. The model will be used for members to evaluate monthly focus.

I’m open to interpretation of the design and artwork. Designers should not feel a need to utilize cliché-like Christian symbols. However, if done minimally (and perhaps first century-like), they could be of interest (but are not required). Keeping it abstract may help readability and convey a roots/back-to-basics feel.

The artwork will be used for a video and PowerPoint presentation. It should be vector-based for simple movement/animation.

Additional thoughts:
Readable, not complex
Interesting interlocking design found at: https://www.pixelvarno.com/ring-module-infographic-choices-segments-stages-layout-loop-diagram-chart-round-graph-image507318264

Target Market(s)

To existing members (for reflection) and for those seeking a simpler church experience.

Requirements
Must have
• Simple, readable design, ability to reproduce for PowerPoint, video, and web. Prefer simple illustrations rather than images.
Nice to have
• The design should create a calming sense of focus on four priorities vs. the complexity of structure/requirements often found in the church experience.
Should not have
• Not crazy about puzzle pieces. Please avoid using all CAPS and serif fonts. Should not use complex images or photos.

```html
<!DOCTYPE html>
<html lang="en">
<head>
<meta charset="utf-8">
<title>House Church Model</title>
<link rel="stylesheet" href="https://fonts.googleapis.com/css2?family=Mulish:wght@300;400&display=swap">
<style>
  :root {
    --navy: #2e23ad;
    --teal: #22ada3;
    --gold: #d4c206;
    --magenta: #8b119b;
    --lavender: #7452b0;
    --paper: #ffffff;
  }
  html, body {
    margin: 0;
    padding: 0;
    width: 1182px;
    height: 1200px;
    overflow: hidden;
    background: var(--paper);
  }
  .model {
    display: block;
    width: 1182px;
    height: 1200px;
    font-family: "Mulish", "Avenir Next", sans-serif;
  }
  .frame { fill: none; stroke: var(--navy); stroke-width: 37; stroke-linejoin: round; }
  .ring { fill: var(--paper); stroke-width: 37; }
  .ring--outreach { stroke: var(--gold); }
  .ring--presence { stroke: var(--magenta); }
  .ring--community { stroke: var(--teal); }
  .ring--discipline { stroke: var(--lavender); }
  .hub { fill: var(--navy); }
  .label { font-weight: 300; font-size: 41px; text-anchor: middle; }
  .label--community { fill: var(--teal); }
  .label--outreach { fill: var(--gold); }
  .label--presence { fill: var(--magenta); font-size: 37px; }
  .label--discipline { fill: var(--lavender); }
  .hub-title { fill: var(--paper); font-weight: 400; font-size: 52px; text-anchor: middle; }
  .sprig { opacity: 0.85; }
</style>
</head>
<body>
<svg class="model" viewBox="0 0 1340 1360" xmlns="http://www.w3.org/2000/svg" aria-labelledby="model-title">
  <title id="model-title">House Church: Community, God's Presence, Discipline, Outreach</title>

  <g class="outer-frame">
    <rect class="frame" x="76" y="61" width="1188" height="1213" rx="6"/>
    <circle class="frame" cx="670" cy="667" r="598"/>
  </g>

  <g class="hallmarks">
    <circle class="ring ring--outreach" cx="376" cy="667" r="207"/>
    <circle class="ring ring--presence" cx="963" cy="667" r="207"/>
    <path class="ring ring--community" d="M 572,592 L 520,520 A 207 207 0 1 1 820,520 L 768,592"/>
    <path class="ring ring--discipline" d="M 572,742 L 520,814 A 207 207 0 1 0 820,814 L 768,742"/>
  </g>

  <g class="hub-group">
    <circle class="hub" cx="670" cy="667" r="155"/>
    <text class="hub-title" x="670" y="655">House</text>
    <text class="hub-title" x="670" y="710">Church</text>
  </g>

  <g class="labels">
    <text class="label label--community" x="667" y="312">Community</text>
    <rect class="sprig" x="613" y="358" width="110" height="20" rx="10" fill="var(--teal)" role="img" aria-label="Small leaf sprig ornament"/>

    <text class="label label--outreach" x="325" y="662">Outreach</text>
    <rect class="sprig" x="297" y="688" width="110" height="20" rx="10" fill="var(--gold)" role="img" aria-label="Small leaf sprig ornament"/>

    <text class="label label--presence" x="1022" y="636">God's</text>
    <text class="label label--presence" x="1022" y="678">Presence</text>
    <rect class="sprig" x="963" y="702" width="110" height="20" rx="10" fill="var(--magenta)" role="img" aria-label="Small leaf sprig ornament"/>

    <text class="label label--discipline" x="667" y="958">Discipline</text>
    <rect class="sprig" x="615" y="1000" width="110" height="20" rx="10" fill="var(--lavender)" role="img" aria-label="Small leaf sprig ornament"/>
  </g>
</svg>
</body>
</html>
```